An our door sign really promoting our clinic and services

We have a new sports medicine clinic called HALLCREST SPORTS MEDICINE.
We want to make a really nice external sign at our clinic using a photo of our team we really like. I have attached the photo.
We want to simply include our LOGO and also signs with these slogan options. So we want different signs with these different slogans so we can choose what we really like.
This should be a simple and quite design.

The SLOGANS WE WOULD LIKE TO SEE ON THE SIGN (only one slogan per sign in the drafts)

1. Your Journey. Our Expertise
2. Where better health begins
3. Building the best version of you
4. Your health, in expert hands
5. Reaching new heights in your health
6. Your path to peak performance starts here

I have also included different versions of our logo based on the background and how you set the sign up

So summary
1. Image attached
2. Slogan options we would like to see them all
3. Logo attached (various options based on how you set the background up)
4. Size of sign is 2935mm wide x 1885mm high

```html
<!DOCTYPE html>
<html lang="en">
<head>
<meta charset="utf-8">
<title>Hallcrest Sports Medicine – Exterior Sign Drafts</title>
<link rel="stylesheet" href="https://fonts.googleapis.com/css2?family=Anton&family=Barlow+Condensed:wght@700&display=swap">
<style>
  :root {
    --page-bg: #b4b4b4;
    --navy: #17194a;
    --sky: #4fc3e8;
    --sky-soft: rgba(100, 205, 240, 0.55);
    --white: #ffffff;
    --photo-light: #c9c6bf;
    --photo-mid: #6f6a62;
    --photo-dark: #2a2b30;
  }
  html, body {
    margin: 0;
    padding: 0;
    width: 1200px;
    height: 2700px;
    overflow: hidden;
    background: var(--page-bg);
  }
  .sign-sheet {
    position: relative;
    width: 1200px;
    height: 2700px;
  }
  /* 2935 × 1885 mm sign, drawn at 965 × 620 px */
  .sign {
    position: absolute;
    left: 118px;
    width: 965px;
    height: 620px;
    box-shadow: 0 2px 6px rgba(0, 0, 0, 0.25);
    background: var(--navy);
  }
  .sign--journey { top: 224px; }
  .sign--health { top: 1011px; }
  .sign--version { top: 1856px; }
  .sign svg {
    display: block;
    width: 100%;
    height: 100%;
  }
  .navy-panel { fill: var(--navy); }
  .accent { fill: var(--sky); }
  .accent-soft { fill: var(--sky-soft); }
  .chip { fill: var(--white); }
  .brand-name {
    font-family: "Barlow Condensed", sans-serif;
    font-weight: 700;
    font-style: normal;
    fill: var(--white);
    letter-spacing: 1px;
  }
  .headline {
    font-family: "Anton", sans-serif;
    font-weight: 400;
    font-style: italic;
  }
  .headline .light { fill: var(--white); }
  .headline .blue { fill: var(--sky); }
</style>
</head>
<body>
<main class="sign-sheet">

  <svg width="0" height="0" style="position:absolute" aria-hidden="true">
    <defs>
      <linearGradient id="team-photo-tone" x1="0" y1="0" x2="0.6" y2="1">
        <stop offset="0" stop-color="var(--photo-light)"/>
        <stop offset="0.45" stop-color="var(--photo-mid)"/>
        <stop offset="1" stop-color="var(--photo-dark)"/>
      </linearGradient>
    </defs>
  </svg>

  <!-- Sign option 1 -->
  <section class="sign sign--journey">
    <svg viewBox="0 0 920 591" preserveAspectRatio="none">
      <g role="img" aria-label="Team photo: a clinician showing a tablet to a client in the clinic gym">
        <polygon points="0,0 557,0 330,591 0,591" fill="url(#team-photo-tone)"/>
      </g>
      <polygon class="accent" points="0,0 120,0 0,120"/>
      <polygon class="accent-soft" points="120,0 160,0 0,160 0,120"/>
      <polygon class="accent-soft" points="505,0 557,0 330,591 300,591"/>
      <polygon class="navy-panel" points="557,0 920,0 920,591 330,591"/>
      <polygon class="accent" points="877,15 907,15 907,45"/>
      <rect class="accent" x="552" y="140" width="26" height="26"/>
      <text class="brand-name" x="590" y="164" font-size="34" textLength="292" lengthAdjust="spacingAndGlyphs">HALLCREST SPORTS MEDICINE</text>
      <text class="headline" x="900" y="339" font-size="100" text-anchor="end" textLength="398" lengthAdjust="spacingAndGlyphs"><tspan class="light">YOUR </tspan><tspan class="blue">JOURNEY</tspan></text>
      <polygon class="accent" points="472,364 920,364 920,448 458,448"/>
      <text class="headline" x="893" y="443" font-size="99" text-anchor="end" textLength="403" lengthAdjust="spacingAndGlyphs"><tspan class="light">OUR EXPERTISE</tspan></text>
      <polygon class="chip" points="428,463 453,463 449,487 424,487"/>
    </svg>
  </section>

  <!-- Sign option 2 -->
  <section class="sign sign--health">
    <svg viewBox="0 0 920 591" preserveAspectRatio="none">
      <g role="img" aria-label="Team photo: a clinician showing a tablet to a client in the clinic gym">
        <polygon points="0,0 557,0 330,591 0,591" fill="url(#team-photo-tone)"/>
      </g>
      <polygon class="accent" points="0,0 120,0 0,120"/>
      <polygon class="accent-soft" points="120,0 160,0 0,160 0,120"/>
      <polygon class="accent-soft" points="505,0 557,0 330,591 300,591"/>
      <polygon class="navy-panel" points="557,0 920,0 920,591 330,591"/>
      <polygon class="accent" points="877,15 907,15 907,45"/>
      <rect class="accent" x="552" y="140" width="26" height="26"/>
      <text class="brand-name" x="590" y="164" font-size="34" textLength="292" lengthAdjust="spacingAndGlyphs">HALLCREST SPORTS MEDICINE</text>
      <text class="headline" x="899" y="342" font-size="102" text-anchor="end" textLength="393" lengthAdjust="spacingAndGlyphs"><tspan class="light">WHERE </tspan><tspan class="blue">BETTER</tspan></text>
      <polygon class="accent" points="472,365 920,365 920,449 458,449"/>
      <text class="headline" x="897" y="445" font-size="100" text-anchor="end" textLength="407" lengthAdjust="spacingAndGlyphs"><tspan class="light">HEALTH BEGINS</tspan></text>
      <polygon class="chip" points="428,463 453,463 449,487 424,487"/>
    </svg>
  </section>

  <!-- Sign option 3 -->
  <section class="sign sign--version">
    <svg viewBox="0 0 920 591" preserveAspectRatio="none">
      <g role="img" aria-label="Team photo: a clinician showing a tablet to a client in the clinic gym">
        <polygon points="0,0 557,0 330,591 0,591" fill="url(#team-photo-tone)"/>
      </g>
      <polygon class="accent" points="0,0 120,0 0,120"/>
      <polygon class="accent-soft" points="120,0 160,0 0,160 0,120"/>
      <polygon class="accent-soft" points="505,0 557,0 330,591 300,591"/>
      <polygon class="navy-panel" points="557,0 920,0 920,591 330,591"/>
      <polygon class="accent" points="877,15 907,15 907,45"/>
      <rect class="accent" x="552" y="140" width="26" height="26"/>
      <text class="brand-name" x="590" y="164" font-size="34" textLength="292" lengthAdjust="spacingAndGlyphs">HALLCREST SPORTS MEDICINE</text>
      <text class="headline" x="902" y="346" font-size="78" text-anchor="end" textLength="400" lengthAdjust="spacingAndGlyphs"><tspan class="light">BUILDING </tspan><tspan class="blue">THE BEST</tspan></text>
      <polygon class="accent" points="466,364 920,364 920,448 452,448"/>
      <text class="headline" x="890" y="439" font-size="96" text-anchor="end" textLength="402" lengthAdjust="spacingAndGlyphs"><tspan class="light">VERSION OF YOU</tspan></text>
      <polygon class="chip" points="421,462 446,462 442,486 417,486"/>
    </svg>
  </section>

</main>
</body>
</html>
```